Fallow Crest Bourbon Barrel Aged Wine

We are taking a sweet red wine and barrel aging it in previously used bourbon barrels. The abv is 16%. Kentucky based. I have attached our Brand logo for reference. Use colors that evoke warmth, richness, and sophistication. We would like to consider a raised or textured label.

Target Market(s)

bourbon and wine drinkers

```html
<!DOCTYPE html>
<html lang="en">
<head>
<meta charset="utf-8">
<title>Fallow Crest Bourbon Barrel Aged Wine – Label</title>
<link rel="stylesheet" href="https://fonts.googleapis.com/css2?family=Cinzel:wght@400;500;600&display=swap">
<style>
  :root {
    --backdrop: #141414;
    --label-dark: #121110;
    --label-warm: #3a2c17;
    --gold: #c9962e;
    --ink-light: #f4f1ea;
    --paper: #ffffff;
    --ink-dark: #1a1a1a;
  }
  * { margin: 0; padding: 0; box-sizing: border-box; }
  html, body {
    width: 1087px; height: 1200px; overflow: hidden;
    background: var(--backdrop);
    font-family: "Cinzel", "Times New Roman", serif;
  }
  .label {
    position: absolute; left: 63px; top: 155px;
    width: 960px; height: 890px;
    background: var(--paper);
  }
  .label__edge {
    position: absolute; left: 0; top: 0; width: 100%; height: 16px;
    display: block;
  }
  .label__panel {
    position: absolute; left: 0; top: 16px; width: 100%; height: 595px;
    background:
      radial-gradient(ellipse 420px 360px at 74% 48%, rgba(90,68,32,0.55), rgba(58,44,23,0.2) 60%, transparent 80%),
      linear-gradient(180deg, #0e0d0c 0%, var(--label-dark) 60%, #1a1814 100%);
  }
  .label__title {
    position: absolute; left: 0; right: 0; top: 140px;
    text-align: center; color: var(--gold);
    font-size: 104px; font-weight: 500; line-height: 1;
    letter-spacing: 2px; white-space: nowrap;
  }
  .label__subtitle {
    position: absolute; left: 0; right: 0; top: 258px;
    display: flex; align-items: center; justify-content: center; gap: 12px;
    color: var(--ink-light); font-size: 38px; line-height: 1; letter-spacing: 1px;
  }
  .label__subtitle::before, .label__subtitle::after {
    content: ""; width: 102px; height: 2px; background: var(--ink-light);
  }
  .label__origin {
    position: absolute; left: 0; right: 0; top: 362px;
    text-align: center; color: var(--ink-light);
    font-size: 46px; line-height: 49px; letter-spacing: 1px;
  }
  .label__seal {
    position: absolute; left: 382px; top: 514px;
    width: 194px; height: 194px; border-radius: 50%;
    background: #1c1b1a;
    display: flex; align-items: center; justify-content: center;
    color: var(--gold); font-size: 22px; font-weight: 500;
    text-align: center; line-height: 1.2; letter-spacing: 1px;
  }
  .details {
    position: absolute; left: 33px; top: 730px;
    width: 576px; height: 125px;
    border: 2px solid var(--ink-dark);
    color: var(--ink-dark); font-size: 13px;
  }
  .details__row {
    position: absolute; left: 0; width: 568px; display: flex;
  }
  .details__row--top { top: 0; height: 59px; border-bottom: 2px solid var(--ink-dark); }
  .details__row--bottom { top: 61px; }
  .details__cell { padding: 4px 8px; height: 52px; }
  .details__cell + .details__cell { border-left: 2px solid var(--ink-dark); }
  .details__cell--volume { width: 146px; }
  .details__cell--age { width: 144px; }
  .details__cell--abv { width: 96px; }
  .details__cell--bottle { flex: 1; border-left-width: 2px; }
  .signature {
    position: absolute; left: 732px; top: 832px; width: 190px;
    border-top: 2px dotted var(--ink-dark);
    padding-top: 9px; text-align: center;
    color: var(--ink-dark); font-size: 14px; letter-spacing: 0.5px;
  }
</style>
</head>
<body>
  <main class="label">
    <svg class="label__edge" role="img" aria-label="Gold sawtooth edge along the top of the label" viewBox="0 0 960 16" preserveAspectRatio="none">
      <rect width="960" height="16" fill="#c9962e"/>
    </svg>
    <section class="label__panel">
      <h1 class="label__title">FALLOW CREST</h1>
      <p class="label__subtitle">BOURBON BARRELS</p>
      <p class="label__origin">KENTUCKY<br>BASED</p>
    </section>
    <div class="label__seal">FALLOW<br>CREST</div>
    <div class="details">
      <div class="details__row details__row--top">
        <div class="details__cell details__cell--volume">VOLUME</div>
        <div class="details__cell details__cell--age">AGE</div>
        <div class="details__cell details__cell--abv">ABV</div>
        <div class="details__cell details__cell--bottle">BOTTLE NO.</div>
      </div>
      <div class="details__row details__row--bottom">
        <div class="details__cell">PROOF</div>
      </div>
    </div>
    <p class="signature">MASTER DISTILEER</p>
  </main>
</body>
</html>
```